MBRT Needs Fundraiser Dinner Invite!!

The Marita Brenkoll Foundation, a 501 3(c) non for profit has a yearly fundraiser, with varying themes. Last year it was "cowboys" and "cowgirls"
This year, it is Parlor 88, or 70's disco music. I have uploaded last years invite for reference, some stock photography for inspiration. You are not limited to using the stock photos.

Annual MBRT Fundraiser Dinner
October 13th, 2022
Starts: 6:30pm
RSVP By: September 20th
Place: The Oxmere
Price: $135 per ticket

Target Market(s)

Donors, Business People, Every person

Industry/Entity Type

Non for Profit

Font styles to use
Sans Serif

Colors
0054AA
0677BA
7BADD7
CADEEF
E8F1F8
E54698
E96AAD
F1A4CE
F9D9EA
FCEFF6
6B429C
8869AF
B7A5CE
E3DAEB
F3F0F8

Requirements
Must have
• The invite should be 5x7, be sophisticated as the clientele are mainly business people that come to support the cause. It should be fun and inviting at the same time.

```html
<!DOCTYPE html>
<html lang="en">
<head>
<meta charset="UTF-8">
<title>MBRT Annual Fundraiser Dinner Invite</title>
<link href="https://fonts.googleapis.com/css2?family=Limelight&family=Montserrat:wght@500;600&display=swap" rel="stylesheet">
<style>
  :root {
    --stage: #1c1c1e;
    --night: #1f0a4a;
    --violet: #3b148a;
    --plum: #6b1f9c;
    --magenta: #c02a9a;
    --pink: #e54698;
    --pink-soft: #f1a4ce;
    --blush: #f9d9ea;
    --ink-light: #fcf2fa;
    --rsvp-line: #e54698;
  }
  * { margin: 0; padding: 0; box-sizing: border-box; }
  html, body { width: 1200px; height: 960px; overflow: hidden; }
  body {
    background: var(--stage);
    font-family: "Montserrat", sans-serif;
    color: var(--ink-light);
  }
  .invite {
    position: absolute;
    left: 280px; top: 32px;
    width: 640px; height: 896px;
    overflow: hidden;
    background:
      radial-gradient(ellipse 70% 30% at 50% 0%, rgba(90,40,200,.55), transparent 70%),
      radial-gradient(ellipse 80% 35% at 50% 100%, rgba(229,70,152,.6), transparent 75%),
      linear-gradient(180deg, var(--violet) 0%, var(--night) 40%, var(--plum) 72%, var(--magenta) 100%);
  }
  .eyebrow {
    position: absolute; top: 48px; left: 0; right: 0;
    display: flex; align-items: center; gap: 14px;
    font-size: 21px; font-weight: 600; letter-spacing: 2.5px;
    white-space: nowrap;
  }
  .eyebrow::before, .eyebrow::after {
    content: ""; flex: 1; height: 2px; background: var(--ink-light);
  }
  .eyebrow::before { flex: 0 0 82px; }
  .eyebrow::after { flex: 1; }
  .monogram {
    position: absolute; top: 92px; left: 0; right: 0;
    text-align: center;
    font-family: "Limelight", serif;
    font-size: 138px; line-height: 1; letter-spacing: 4px;
    color: var(--blush);
  }
  .foundation {
    position: absolute; top: 232px; left: 0; right: 0;
    text-align: center; font-size: 16px; font-weight: 600; letter-spacing: 2px;
    text-transform: uppercase;
  }
  .divider {
    position: absolute; top: 264px; left: 245px; width: 150px; height: 2px;
    background: var(--ink-light);
  }
  .details {
    position: absolute; top: 286px; left: 0; right: 0;
    text-align: center; text-transform: uppercase; font-weight: 500;
  }
  .details .date { font-size: 25px; letter-spacing: 3.5px; line-height: 44px; }
  .details .venue { font-size: 30px; letter-spacing: 4px; line-height: 44px; }
  .details .doors { font-size: 23px; letter-spacing: 3.5px; line-height: 44px; }
  .butterfly {
    position: absolute; width: 72px; height: 62px; border-radius: 50%;
    background: radial-gradient(circle, rgba(252,242,250,.55), rgba(252,242,250,.1) 70%, transparent);
  }
  .butterfly.top-left { left: 28px; top: 140px; }
  .butterfly.top-right { left: 540px; top: 148px; }
  .butterfly.bottom-left { left: 28px; top: 814px; }
  .butterfly.bottom-right { left: 560px; top: 814px; }
  .sphere {
    position: absolute; width: 220px; height: 220px; border-radius: 50%;
    background: radial-gradient(circle at 38% 30%, var(--blush) 0%, var(--pink-soft) 30%, var(--pink) 68%, #b8389a 100%);
    box-shadow: 0 0 40px rgba(229,70,152,.35);
  }
  .sphere.left { left: -3px; top: 434px; }
  .sphere.right { left: 434px; top: 434px; }
  .price {
    position: absolute; left: 36px; top: 496px;
    transform: rotate(-32deg); transform-origin: left center;
    display: flex; align-items: flex-end; gap: 4px;
  }
  .price .amount { font-size: 46px; font-weight: 600; line-height: 1; }
  .price .unit { font-size: 13px; font-weight: 600; letter-spacing: 1.5px; padding-bottom: 6px; }
  .sphere-name {
    position: absolute; left: 470px; top: 528px; width: 150px;
    text-align: center; font-size: 13px; font-weight: 500; line-height: 1.35;
    color: rgba(252,242,250,.75);
  }
  .disco-ball {
    position: absolute; left: 157px; top: 458px; width: 356px; height: 356px; border-radius: 50%;
    background:
      radial-gradient(circle at 40% 30%, #f6c9f2 0%, #d97be6 35%, #a93fc9 70%, #7a2aa4 100%);
    box-shadow: 0 0 50px rgba(200,90,230,.45);
  }
  .rsvp {
    position: absolute; top: 818px; left: 116px; width: 408px; height: 46px;
    border: 2px solid var(--rsvp-line);
    display: flex; align-items: center; justify-content: center;
    font-size: 20px; font-weight: 600; letter-spacing: 2.5px; text-transform: uppercase;
  }
</style>
</head>
<body>
  <main class="invite">
    <p class="eyebrow">Annual Fundraiser Dinner</p>
    <div class="butterfly top-left" role="img" aria-label="White butterfly illustration"></div>
    <h1 class="monogram">MBRT</h1>
    <div class="butterfly top-right" role="img" aria-label="White butterfly illustration"></div>
    <p class="foundation">The Marita Brenkoll Foundation</p>
    <div class="divider"></div>
    <div class="details">
      <p class="date">October 13th, 2022</p>
      <p class="venue">At The Oxmere</p>
      <p class="doors">Doors open at 6:30pm</p>
    </div>
    <div class="sphere left"></div>
    <div class="sphere right"></div>
    <p class="price"><span class="amount">$135</span><span class="unit">PER TICKET</span></p>
    <p class="sphere-name">The Marita Brenkoll Foundation</p>
    <div class="disco-ball" role="img" aria-label="Pink mirrored disco ball illustration"></div>
    <div class="butterfly bottom-left" role="img" aria-label="White butterfly illustration"></div>
    <p class="rsvp">RSVP by September 20th</p>
    <div class="butterfly bottom-right" role="img" aria-label="White butterfly illustration"></div>
  </main>
</body>
</html>
```